Brivtel sales folder inserts

We need the same design for 4 separate service offerings to put inside our sales folder. Each insert should be laid out the same with different images and text and the 2nd, 3rd, and 4th should each be 3/4" shorter than the previous one so that when all 4 are inserted into the folder you see the black strip with text showing what the service offering is. Basically staggered inserts.

Industry/Entity Type

Information Technology

Font styles to use
Sans Serif

Colors
acd136

Requirements
Must have
• Brivtel logo and included text. Keep with the green Pantone 90 and black color scheme
Nice to have
• a better layout and pics

```html
<!DOCTYPE html>
<html lang="en">
<head>
<meta charset="utf-8">
<title>Brivtel sales folder inserts</title>
<link href="https://fonts.googleapis.com/css2?family=Roboto:wght@500;700;900&family=Open+Sans:wght@600&family=Arimo:wght@400;700&display=swap" rel="stylesheet">
<style>
:root{
  --green:#acd136;
  --green-deep:#5f7a14;
  --ink:#231f20;
  --stage:#2b2b2b;
  --paper:#ffffff;
  --text:#3a3a3a;
}
*{box-sizing:border-box;margin:0;padding:0}
html,body{width:1200px;height:2430px;overflow:hidden;background:var(--stage)}
body{position:relative;font-family:"Arimo",Arial,sans-serif;color:var(--text)}

.insert{position:absolute;height:709px;background:var(--paper);overflow:hidden}
.insert-business{left:55px;top:71px;width:549px}
.insert-it{left:649px;top:71px;width:495px}
.insert-secure{left:55px;top:819px;width:473px}
.insert-voice{left:562px;top:819px;width:435px}

.edge{position:absolute;left:0;top:0;bottom:0;width:14px;background:var(--ink)}
.edge-tab{position:absolute;left:0;bottom:0;width:22px;background:var(--ink);border-top-right-radius:14px}
.insert-it .edge-tab{top:280px}
.insert-voice .edge-tab{top:360px}

.hero{position:absolute;left:14px;right:0;top:0;height:138px;
  background:linear-gradient(90deg,#fff 0%,#fff 40%,#c9d98f 56%,#7f9a2a 72%,#3d5210 88%,#22300a 100%)}
.hero-line{position:absolute;left:14px;right:0;top:138px;height:3px;background:var(--green)}

.brand{position:absolute;left:52px;top:32px;display:flex;align-items:center;gap:12px;padding:6px 10px;background:#fff}
.brand-mark{width:30px;height:30px;background:var(--green)}
.brand-name{font-family:"Roboto",sans-serif;font-weight:700;font-size:19px;letter-spacing:2px;color:var(--green-deep);text-transform:lowercase}

.title-back{position:absolute;left:32px;top:141px;width:264px;height:40px;background:var(--ink);
  clip-path:polygon(0 0,100% 0,92% 100%,0 100%)}
.title{position:absolute;left:32px;top:141px;width:250px;height:37px;background:var(--green);
  clip-path:polygon(0 0,100% 0,91% 100%,0 100%);
  font-family:"Roboto",sans-serif;font-weight:900;font-size:16px;color:var(--ink);
  padding:10px 0 0 16px;letter-spacing:.2px;white-space:nowrap}
.insert-voice .title-back{width:308px}
.insert-voice .title{width:294px}

.spine{position:absolute;left:14px;top:200px;bottom:140px;width:26px;display:flex;align-items:center;justify-content:center}
.spine span{writing-mode:vertical-rl;transform:rotate(180deg);white-space:nowrap;
  font-family:"Open Sans",sans-serif;font-weight:600;font-size:14.5px;color:var(--green);letter-spacing:.3px}
.insert-it .spine{left:26px;top:300px;bottom:120px}
.insert-secure .spine{top:340px;bottom:110px}
.insert-voice .spine{left:26px;top:375px;bottom:45px}

.content{position:absolute;left:60px;right:0;top:205px;bottom:46px;display:grid;grid-template-columns:1fr 1fr;gap:12px}
.col{display:flex;flex-direction:column;font-size:7.2px;line-height:1.38}
.col p{margin-bottom:7px}
.col p.lead{margin-bottom:10px}
.col p.after-visual{margin-top:40px}
.col strong{color:var(--ink)}

.lead-head{border-bottom:2px solid var(--ink);margin-bottom:14px}
.lead-head span{display:block;width:88%;background:var(--green);color:var(--ink);
  font-family:"Roboto",sans-serif;font-weight:700;font-size:10px;padding:3px 6px;
  clip-path:polygon(0 0,100% 0,94% 100%,0 100%)}

.list-head{background:var(--ink);color:var(--green);font-family:"Arimo",sans-serif;font-weight:700;
  font-size:7.6px;padding:4px 6px;margin:0 0 6px 0}
.checks{list-style:none;margin:0 0 6px 0;padding-right:10px}
.checks li{position:relative;padding-left:16px;margin-bottom:8px}
.checks li::before{content:"";position:absolute;left:2px;top:1px;width:6px;height:6px;border:1px solid #555}
.checks li::after{content:"";position:absolute;left:4px;top:1px;width:2px;height:4px;border:solid #333;border-width:0 1px 1px 0;transform:rotate(40deg)}

.visual{width:100%;margin-bottom:14px}
.v-circuit{height:170px;background:radial-gradient(circle at 50% 40%,#c9df6a,#5d7a17 45%,#1e2a07 100%)}
.v-drive{height:192px;margin-top:auto;background:radial-gradient(circle at 60% 45%,#b8d85a,#3f6a1f 40%,#0d1f14 90%)}
.v-dash{height:168px;background:linear-gradient(180deg,#e9edf1,#d4dce3);border:1px solid #ccc}
.v-chart{height:142px;margin-top:auto;background:linear-gradient(180deg,#f5f5f5,#d8dbe4)}
.v-gauge{height:172px;background:radial-gradient(circle at 40% 60%,#5d7280,#1f2a31 60%,#0e1419)}
.v-cameras{height:80px;margin-top:auto;background:linear-gradient(90deg,#dcdcdc,#8a8a8a 50%,#e4e4e4)}
.v-options{height:150px;width:86%;background:radial-gradient(circle at 50% 50%,#6aa0e0,#1f4c9a 60%,#0c2a66)}
.v-thinker{height:196px;margin-top:28px;background:radial-gradient(circle at 55% 30%,#e6efc6,#fff 70%)}

.foot-line{position:absolute;left:14px;right:0;bottom:0;height:3px;background:var(--ink)}
.foot{position:absolute;left:100px;right:0;bottom:3px;height:28px;background:var(--green);
  border-top-left-radius:40px 28px;display:flex;align-items:center;justify-content:center;
  font-family:"Roboto",sans-serif;font-weight:700;font-size:11px;color:var(--ink);white-space:nowrap}
.insert-voice .foot{left:60px;font-size:10px}
</style>
</head>
<body>

<section class="insert insert-business">
  <div class="hero" role="img" aria-label="Green-toned image of a hand holding a globe with connected devices and people"></div>
  <div class="hero-line"></div>
  <div class="edge"></div>
  <div class="brand"><span class="brand-mark"></span><span class="brand-name">Brivtel</span></div>
  <div class="title-back"></div>
  <h1 class="title">ALL-BUSINESS</h1>
  <div class="spine"><span>ALL-BUSINESS RUN ANYWHERE, PROTECT ANYTHING</span></div>
  <div class="content">
    <div class="col">
      <h2 class="lead-head"><span>Run Anywhere, Protect Anything</span></h2>
      <p class="lead"><strong>Your Business Continuity Solution.</strong><br>Brivtel's ALL-BUSINESS solution provides comprehensive backups for your data like never before.</p>
      <div class="visual v-circuit" role="img" aria-label="Green circuit board with a padlock at its centre"></div>
      <p>In todays environment threats are never ending. There is always a new threat trying to get to your data, whether to Kryptex lock it and hold it for ransom, or be malicious and delete it for no reason at all.</p>
      <p>Keeping your network up to date and monitoring for suspicious activity are all recommended actions, but backing up your data is the most important action you can take.</p>
      <p>Don't just back up your data. Verify it. What good is a backup of your data if it does not work when you need it. The Brivtel ALL-Business solution tests and verifies your data on a daily basis.</p>
      <p>The ALL-Business solution also provides you a local and an off-site copy of your data. What good is a business continuity plan if your backups burn down with your building.</p>
      <p>The ALL-Business solution provides an onsite server resource should you need it, as well as allowing you to spin up virtual servers in the cloud during a disaster scenario.</p>
    </div>
    <div class="col">
      <h3 class="list-head">Does your backup solution do this?</h3>
      <ul class="checks">
        <li>Test and verify your backups by booting on a virtual server in the cloud</li>
        <li>Backup your WorkSuite 365</li>
        <li>Allow you to spin up virtual servers in the cloud during a disaster</li>
      </ul>
      <h3 class="list-head">Did You Know?</h3>
      <ul class="checks">
        <li>60% of backups are incomplete</li>
        <li>50% of restores fail</li>
        <li>40% of the SMB market will be attacked by a hacker, 50% wont even know it.</li>
        <li>20% of SMB market will lose critical data every 5-years</li>
        <li>90% of business that lost data for 10-days or more filed for bankruptcy immediately</li>
      </ul>
      <div class="visual v-drive" role="img" aria-label="Close-up of an open hard drive platter in green light"></div>
    </div>
  </div>
  <div class="foot-line"></div>
  <div class="foot">A Little Mistake Can Cost a Fortune</div>
</section>

<section class="insert insert-it">
  <div class="hero" role="img" aria-label="Green glowing circuit board with a central processor"></div>
  <div class="hero-line"></div>
  <div class="edge"></div>
  <div class="edge-tab"></div>
  <div class="brand"><span class="brand-mark"></span><span class="brand-name">Brivtel</span></div>
  <div class="title-back"></div>
  <h1 class="title">ALL-IT</h1>
  <div class="spine"><span>ALL-IT PROACTIVE IT SUPPORT</span></div>
  <div class="content">
    <div class="col">
      <h2 class="lead-head"><span>A True IT Partnership</span></h2>
      <p class="lead"><strong>An IT partner not provider.</strong><br>We understand why your critical business services are so important to your daily operations. This is why we spend so much time aligning our technology support with just such business services. Building a program that relies on 24x7x365 network monitoring coupled with an aggressive preventative maintenance component to ensure optimum uptime for your business.</p>
      <div class="visual v-dash" role="img" aria-label="Screenshot of a network monitoring dashboard with tables and traffic graphs"></div>
      <p>One of the major challenges in maintaining a computer network is trying to predict what will fail and when. With our ALL-IT solution, we can prevent many network failures from ever happening. By combining regular and comprehensive preventative maintenance and robust real-time monitoring of your critical network and desktop devices, we ensure the reliability and stability of your IT assets.</p>
      <p>This solution is so effective, our customers see almost immediate results. A regularly maintained network means fewer failures, yielding higher productivity and savings on support costs for you.<br>At the same time, your exposure to security risks is dramatically lessened, and frustration from unstable IT resources almost vanishes. We allow our customers to focus on their core business functions by taking the worry out of owning a computer network.</p>
    </div>
    <div class="col">
      <h3 class="list-head">Do these issues plague your business?</h3>
      <ul class="checks">
        <li><strong>Network neglected?</strong> Is yours perceived as a "necessary evil" and not as integral to improving business performance?</li>
        <li><strong>Downtime impact?</strong> Are IT outages distracting your staff from their core focus, or prohibiting them from working efficiently?</li>
        <li><strong>Distracted employees?</strong> Do your staff rely on other non-IT employees to deal with distracting IT problems?</li>
      </ul>
      <h3 class="list-head">Program Advantages:</h3>
      <ul class="checks">
        <li><strong>Increased productivity:</strong> Continuous insight into your network lets us reduce the business impact of IT failure by shortening the time from network failure to issue resolution.</li>
        <li><strong>Reduced business impact from IT failures:</strong> Combining preventative maintenance and remote monitoring means we minimize failures that could impact your business. Your network behaves in a stable and reliable manner.</li>
        <li><strong>Reduced network downtime through proactive maintenance:</strong> Through regular, preventative maintenance activities designed to keep your network operating efficiently, we reduce the number of emergency incidents you encounter.</li>
      </ul>
      <div class="visual v-chart" role="img" aria-label="Glasses and a pen resting on a printed bar chart"></div>
    </div>
  </div>
  <div class="foot-line"></div>
  <div class="foot">Stop Buying Downtime – Invest in Uptime</div>
</section>

<section class="insert insert-secure">
  <div class="hero" role="img" aria-label="Green digital circuitry with a padlock icon"></div>
  <div class="hero-line"></div>
  <div class="edge"></div>
  <div class="brand"><span class="brand-mark"></span><span class="brand-name">Brivtel</span></div>
  <div class="title-back"></div>
  <h1 class="title">ALL-SECURE</h1>
  <div class="spine"><span>ALL-SECURE SECURE YOUR ASSETS</span></div>
  <div class="content">
    <div class="col">
      <h2 class="lead-head"><span>ALL-SECURE Security at its Best</span></h2>
      <p class="lead"><strong>ALL-SECURE provides piece of mind.</strong><br>Secure your company with industry leading cameras and door access systems.<br>Monitor your business like you monitor your accounts.</p>
      <div class="visual v-gauge" role="img" aria-label="Dial gauge with a needle pointing to the word security"></div>
      <p>Brivtel provides network video recorders and IP-CCTV cameras with intelligence. Keeping an eye on your business 24X7 is essential in todays environment. Whether the problem is shrinking inventory, unauthorized access, or performance, keeping an eye on things is essential.</p>
      <p>Having the ability to go back in time and review what happened is becoming more important by the day. Having a video of an incident can mean the difference between settling out of court or dismissing of the case entirely.</p>
      <p>Securing your entry points to your site is crucial. With a card access system from Brivtel you will have control of who has access and when. You will have the ability to control ingress and egress to specific areas. Never have to worry about lost keys, with card access you delete the card and your secure.</p>
    </div>
    <div class="col">
      <h3 class="list-head">Do I need these types of systems?</h3>
      <ul class="checks">
        <li>I use hard keys? Hard keys can be lost, copied, and not returned. Card access provides you control over these problems.</li>
        <li>I trust my people, I don't need to have video cameras? This is not a matter of trust, it is a matter of security. You can allow employees access to viewing certain cameras to provide a level of security.</li>
        <li>This sounds complicated? Brivtel can provide complete management of these systems so you never have to wonder how this works. A single call gets it all done now, call Brivtel.</li>
      </ul>
      <h3 class="list-head">What Can I Do With These Systems?</h3>
      <ul class="checks">
        <li>Receive alerts according to events</li>
        <li>Review events of the past</li>
        <li>Increase security with access events</li>
        <li>Enhanced reporting capabilities</li>
        <li>View video from anywhere</li>
        <li>End lost or copied keys</li>
        <li>Provide employees piece of mind</li>
        <li>24X7 On Call Services</li>
      </ul>
      <div class="visual v-cameras" role="img" aria-label="Security cameras, a keypad reader and a video recorder"></div>
    </div>
  </div>
  <div class="foot-line"></div>
  <div class="foot">Secure Your Assets</div>
</section>

<section class="insert insert-voice">
  <div class="hero" role="img" aria-label="Green-tinted digital assistant visual with a glowing ring"></div>
  <div class="hero-line"></div>
  <div class="edge"></div>
  <div class="edge-tab"></div>
  <div class="brand"><span class="brand-mark"></span><span class="brand-name">Brivtel</span></div>
  <div class="title-back"></div>
  <h1 class="title">ALL-VOICE, EVERY OPTION</h1>
  <div class="spine"><span>ALL-SECURE SECURE YOUR ASSETS</span></div>
  <div class="content">
    <div class="col">
      <h2 class="lead-head"><span>A True IT Partnership</span></h2>
      <p class="lead"><strong>ALL-VOICE provides endless options.</strong><br>Working with Brivtel provides you with options. We work with every provider so you can select the best option for your needs.</p>
      <div class="visual v-options" role="img" aria-label="Hand pointing at five numbered option buttons on a blue background"></div>
      <p class="after-visual">Brivtel offers both On-Premise Unified Communication solutions and Hosted Unified Communication solutions.</p>
      <p>No matter what your need is Brivtel has the solution with our ALL-Voice program.</p>
      <p>Brivtel has relationships with almost every provider for internet and voice connections for your business.</p>
      <p>We can provide quotes from any provider in the area.</p>
      <p>More options can mean larger savings. You will have the information to make the best selection for your business needs.</p>
    </div>
    <div class="col">
      <h3 class="list-head">How can Brivtel assist?</h3>
      <ul class="checks">
        <li>Provide multiple options for review</li>
        <li>Provide cost savings</li>
        <li>Educate client on options</li>
        <li>Locate possible cost over runs on existing provider solutions</li>
        <li>Provide turn key solutions</li>
        <li>Provide On-Premise Solutions</li>
        <li>Provide Hosted Solutions</li>
        <li>Multi-site and remote worker solutions</li>
        <li>Contact center solutions</li>
        <li>Multi media Contact Center Solutions</li>
        <li>Advance Reporting and Monitoring</li>
      </ul>
      <div class="visual v-thinker" role="img" aria-label="Illustration of a puzzled businessman under a green thought bubble asking what should I do"></div>
    </div>
  </div>
  <div class="foot-line"></div>
  <div class="foot">Give Yourself Options, and We Can Help You Choose the Right Option</div>
</section>

</body>
</html>
```